Direct to Consumer extended service contract business with a new disruptive business model needs a

We need a customized wordpress design for a company called 'Tall Harbor Assurance'.
We provide an innovative and unique service contract protection program direct to consumers. This program provides monthly coverage for all electronics purchased in the last 4 years and all electronics the consumer purchases in the future for a low monthly fee. The overall design should communicate a sense of legitimacy, ethics, and superior customer service and support (in an industry that has a huge PR issue to overcome).
Electronics is the first product group, other product groups with different price points to launch in the future..

Target Market(s)

All purchasers of electronic goods...all demographics

Industry/Entity Type

Electronics

Font styles to use
Sans Serif

Requirements
Must have
• Customer Testimonials
Industry News
Customer ratings
Blog posts
Call to action messaging
Like the functional elements and design of bramblequill.example (need to be better)
Nice to have
• Like to see video testimonials
Social network "whats trending related to electronics or service contract industry"
Easy way to register products for warranty

```html
<!DOCTYPE html>
<html lang="en">
<head>
<meta charset="utf-8">
<title>Tall Harbor Assurance – Membership</title>
<link rel="stylesheet" href="https://fonts.googleapis.com/css2?family=Noticia+Text:wght@400;700&family=PT+Sans:wght@400;700&display=swap">
<style>
  :root {
    --accent: #f7861c;
    --nav-active: #e9e3e3;
    --hero-grey: #6b6b6b;
    --screen-black: #000000;
    --bar-black: #000000;
    --text-light: #ffffff;
    --text-dark: #3a3a3a;
  }
  * { box-sizing: border-box; margin: 0; padding: 0; }
  html, body { width: 1200px; height: 555px; overflow: hidden; }
  body {
    position: relative;
    font-family: "PT Sans", Tahoma, sans-serif;
    color: var(--text-light);
    background: var(--hero-grey);
  }
  .site-nav {
    position: absolute; top: 0; left: 0; width: 1200px; height: 44px;
    background: linear-gradient(90deg, #1b1d1c 0%, #2a2f2b 60%, #3b4238 85%, #2c302b 100%);
    border-top: 2px solid var(--accent);
  }
  .site-nav ul {
    list-style: none; display: flex; position: absolute; left: 243px; top: 0; height: 42px;
  }
  .site-nav li a {
    display: block; height: 42px; line-height: 42px; padding: 0 8px;
    font-size: 13.3px; color: var(--text-light); text-decoration: none; margin-right: 23.5px;
  }
  .site-nav li.is-active a { background: var(--nav-active); color: var(--text-dark); }
  .hero-media {
    position: absolute; top: 44px; left: 0; width: 1200px; height: 416px;
    background:
      linear-gradient(var(--screen-black), var(--screen-black)) 250px 49px / 686px 367px no-repeat,
      linear-gradient(#050505, #050505) 135px 375px / 369px 41px no-repeat,
      linear-gradient(#050505, #050505) 821px 376px / 218px 40px no-repeat,
      var(--hero-grey);
  }
  .hero-copy {
    position: absolute; top: 44px; left: 0; width: 1200px; text-align: center;
  }
  .hero-title {
    font-family: "Noticia Text", Georgia, serif; font-weight: 400;
    font-size: 39px; line-height: 1; margin-top: 120px;
  }
  .hero-lead { font-size: 13.4px; margin-top: 17px; }
  .hero-price {
    font-family: "Noticia Text", Georgia, serif; font-weight: 400;
    font-size: 36.5px; line-height: 1; margin-top: 28px;
  }
  .hero-perks { list-style: none; margin-top: 22px; font-size: 13.3px; line-height: 20.5px; }
  .hero-perks svg { width: 11px; height: 9px; margin-right: 2px; vertical-align: -1px; }
  .hero-note { font-size: 10.8px; margin-top: 19px; }
  .cta-bar {
    position: absolute; top: 460px; left: 0; width: 1200px; height: 95px;
    background: var(--bar-black); border-top: 1px solid #4a4a4a;
    display: flex; align-items: center; justify-content: center; gap: 13px;
  }
  .cta-bar-text { font-size: 28px; margin-top: -3px; }
  .cta-button {
    display: inline-block; width: 143px; height: 37px; line-height: 37px;
    background: var(--accent); color: var(--text-light); text-align: center;
    font-family: Arial, "PT Sans", sans-serif; font-size: 18.5px;
    border-radius: 3px; text-decoration: none;
  }
</style>
</head>
<body>
  <nav class="site-nav">
    <ul>
      <li class="is-active"><a href="#">Home</a></li>
      <li><a href="#">Membership Plans</a></li>
      <li><a href="#">Benefits</a></li>
      <li><a href="#">FAQ’s</a></li>
      <li><a href="#">About Us</a></li>
      <li><a href="#">Contact Us</a></li>
      <li><a href="#">News</a></li>
      <li><a href="#">Checkout</a></li>
    </ul>
  </nav>

  <div class="hero-media" role="img" aria-label="Photo of a laptop and two tablets with dark screens on a grey backdrop"></div>

  <section class="hero-copy">
    <h1 class="hero-title">Join the Tall Harbor Assurance Group</h1>
    <p class="hero-lead">Join us for one low monthly membership fee of $19.95 per month and get all your existing and future electronic product purchases protected for free.*</p>
    <p class="hero-price">$19.95 per month</p>
    <ul class="hero-perks">
      <li><svg viewBox="0 0 11 9"><path d="M1 5l3 3 6-7" fill="none" stroke="#fff" stroke-width="2"/></svg>No long term contract commitments</li>
      <li><svg viewBox="0 0 11 9"><path d="M1 5l3 3 6-7" fill="none" stroke="#fff" stroke-width="2"/></svg>Fully Insured</li>
      <li><svg viewBox="0 0 11 9"><path d="M1 5l3 3 6-7" fill="none" stroke="#fff" stroke-width="2"/></svg>Pay as you go – Cancel at any time</li>
    </ul>
    <p class="hero-note">* One time activation fee of $30.00 when joining for the first time.</p>
  </section>

  <section class="cta-bar">
    <span class="cta-bar-text">Join the Tall Harbor Assurance Group</span>
    <a class="cta-button" href="#">Signup Now</a>
  </section>
</body>
</html>
```